Business Card for my Photography/Video Business

I would like the card to say Event Photographer and Videographer. I like the Black and Gold look to it as well but open to other options. I don't want it to be super vibrant or colorful. Simple, elegant and professional

```html
<!DOCTYPE html>
<html lang="en">
<head>
<meta charset="utf-8">
<title>Lumen Reel — Business Card</title>
<link href="https://fonts.googleapis.com/css2?family=Lato:wght@400;700&family=Montserrat:wght@600&display=swap" rel="stylesheet">
<style>
  :root {
    --backdrop: #2a2a2a;
    --card: #1b1b1b;
    --gold-light: #f6e27a;
    --gold: #d4af37;
    --gold-deep: #a8801a;
    --text-light: #ececec;
  }
  * { box-sizing: border-box; margin: 0; padding: 0; }
  html, body { width: 1200px; height: 900px; overflow: hidden; }
  body {
    background: var(--backdrop);
    display: flex;
    flex-direction: column;
    align-items: center;
    justify-content: center;
    gap: 60px;
    font-family: "Lato", Arial, sans-serif;
  }
  .card-frame {
    width: 580px;
    height: 330px;
    padding: 4px;
    border-radius: 18px;
    background: linear-gradient(135deg, var(--gold-deep), var(--gold-light) 30%, var(--gold) 55%, var(--gold-light) 80%, var(--gold-deep));
    box-shadow: 0 10px 30px rgba(0,0,0,.45);
  }
  .card {
    width: 100%;
    height: 100%;
    border-radius: 14px;
    background: var(--card);
    position: relative;
    overflow: hidden;
  }
  .gold-disc {
    border-radius: 50%;
    background: radial-gradient(circle at 35% 35%, var(--gold-light), var(--gold) 50%, var(--gold-deep));
  }

  /* Front */
  .front-brand {
    position: absolute;
    left: 50%;
    top: 118px;
    transform: translateX(-50%);
    display: flex;
    align-items: center;
    gap: 22px;
    white-space: nowrap;
  }
  .front-brand .gold-disc { width: 96px; height: 96px; }
  .brand-name {
    font-family: "Montserrat", Arial, sans-serif;
    font-weight: 600;
    font-size: 50px;
    letter-spacing: 4px;
    color: var(--gold);
  }
  .website {
    position: absolute;
    left: 0; right: 0;
    bottom: 48px;
    text-align: center;
    font-size: 13px;
    letter-spacing: 4px;
    color: var(--gold);
  }

  /* Back */
  .back .gold-disc {
    position: absolute;
    left: 105px;
    top: 105px;
    width: 120px;
    height: 120px;
  }
  .divider {
    position: absolute;
    left: 292px;
    top: 50px;
    width: 2px;
    height: 190px;
    background: linear-gradient(to bottom, var(--gold), rgba(212,175,55,0));
  }
  .contact {
    position: absolute;
    left: 316px;
    right: 28px;
    top: 62px;
    color: var(--text-light);
  }
  .person-name { color: var(--gold); font-size: 16px; font-weight: 700; }
  .person-role { font-size: 13px; margin-top: 3px; }
  .contact-list { list-style: none; margin-top: 26px; }
  .contact-list li {
    display: flex;
    align-items: center;
    gap: 10px;
    font-size: 12px;
    margin-bottom: 9px;
  }
  .contact-list svg { width: 13px; height: 13px; fill: var(--gold); flex: none; }
  .address { color: var(--gold); font-weight: 700; font-size: 13px; margin-top: 6px; white-space: nowrap; }
</style>
</head>
<body>

  <div class="card-frame">
    <section class="card front">
      <div class="front-brand">
        <span class="gold-disc"></span>
        <span class="brand-name">LUMEN REEL</span>
      </div>
      <p class="website">www.lumenreelphoto.com</p>
    </section>
  </div>

  <div class="card-frame">
    <section class="card back">
      <span class="gold-disc"></span>
      <span class="divider"></span>
      <div class="contact">
        <p class="person-name">Dale Morrow</p>
        <p class="person-role">Event Photographer and Videographer</p>
        <ul class="contact-list">
          <li>
            <svg viewBox="0 0 16 16" aria-hidden="true"><path d="M3 1h3l1.5 4-2 1.2a9 9 0 0 0 4.3 4.3L11 8.5l4 1.5v3a2 2 0 0 1-2 2A12 12 0 0 1 1 3a2 2 0 0 1 2-2z"/></svg>
            555 210 4417
          </li>
          <li>
            <svg viewBox="0 0 16 16" aria-hidden="true"><path d="M4 1h8v4H4zM1 6h14v6h-3v3H4v-3H1zM5 10v4h6v-4z"/></svg>
            555 380 6192
          </li>
          <li>
            <svg viewBox="0 0 16 16" aria-hidden="true"><path d="M1 3h14v10H1zM2.5 4.5 8 9l5.5-4.5v-.1h-11z"/></svg>
            dmorrow@lumenreelphoto.com
          </li>
        </ul>
        <p class="address">2270 Harbor Ln, Fairview GA 30100</p>
      </div>
    </section>
  </div>

</body>
</html>
```